Trendy Stylish Safety/Sports glasses polybag and box packaging

Polybag artwork required for safety glasses.
Polybag artwork required for sports glasses.
Packing box artwork required to tie in with polybag packaging.

Both bags to be similar, however one for safety glasses and one for sports glasses.
Maybe touch of different colours to differentiate.

Polybag Packaging for safety glasses.
1. Text to be white on black or vice versa, with a touch of yellow
2. Karnu logos to use, attached.
3. Front of bag to have clear vision panel on RH side
4. Bullet points can be on this clear vision panel.
5. Strapline to be on front of bag after ‘karNUsafety’ is COMFORT…STYLE…PROTECTION
6. Happy to have a touch of other colours on the packet to brighten up, make distinctive.
7. RH side at top on reverse of bag, bar code label to be attached, so this section to be left clear
8. Could have a few safety symbols on possibly.
9. Full text required on polybag is in file ‘safety packaging bag info.docx’

Polybag packaging for sports glasses

1. Text to be white on black or vice versa, with a touch of blue
5. Strapline to be on front of bag after ‘karNUsports’ is PERFORMANCE.…STYLE…PROTECTION
8. Full text required on polybag is in file ‘SPORTS packaging BAG Details.docx’
We havent decided on text for the reverse of this bag, however once we have the basic layout, we can add text at a later stage.

Cardboard packing/posting box for case.

We will use these boxes to pack and despatch our sports and safety glasses.

1. Two long sides of box to match polybag karNU safety design.
Text required on safety sides of box
karNUsafety logo
COMFORT, STYLE, PROTECTION
2. Two long sides of box to match polybag karNU sports design.
3. Text required on sports sides of box
karNUsports logo
PERFORMANCE, STYLE, PROTECTION
4. case box jpg has sizes required
Example of packing box picture attached.

```html
<!DOCTYPE html>
<html lang="en">
<head>
<meta charset="utf-8">
<title>karNUsports – Sports Glasses Polybag</title>
<link rel="stylesheet" href="https://fonts.googleapis.com/css2?family=Didact+Gothic&family=Jost:wght@500;600&display=swap">
<style>
  :root {
    --page: #ffffff;
    --bag-black: #050505;
    --panel-white: #ffffff;
    --ink: #111111;
    --accent-blue: #1b8fd6;
    --accent-blue-deep: #0f76bd;
    --clear-light: #f4f4f4;
    --clear-mid: #d6d6d6;
    --clear-edge: #9a9a9a;
  }
  * { margin: 0; padding: 0; box-sizing: border-box; }
  html, body { width: 1200px; height: 1200px; overflow: hidden; background: var(--page); }
  .canvas { position: relative; width: 1200px; height: 1200px; }

  .polybag {
    position: absolute; left: 398px; top: 68px; width: 402px; height: 1056px;
    background: var(--bag-black); border: 1px solid var(--clear-edge);
  }
  .hang-hole {
    position: absolute; left: 144px; top: 39px; width: 113px; height: 23px;
    background: var(--page); border-radius: 12px;
  }
  .splash-decoration {
    position: absolute; left: 248px; top: 18px; width: 152px; height: 150px;
    background: radial-gradient(circle at 55% 40%, var(--accent-blue) 0%, var(--accent-blue) 38%, rgba(27,143,214,0.5) 55%, rgba(27,143,214,0) 72%);
  }
  .header-rule {
    position: absolute; left: 0; right: 0; top: 182px; height: 1px; background: #222;
  }
  .brand-name {
    position: absolute; left: 36px; top: 88px;
    font-family: "Jost", sans-serif; font-weight: 600; font-size: 27px;
    color: #fff; letter-spacing: 0.5px;
  }
  .strapline {
    position: absolute; left: 36px; top: 124px;
    font-family: "Didact Gothic", sans-serif; font-size: 11.5px; color: #fff; letter-spacing: 0.3px;
  }
  .strapline .divider { color: var(--accent-blue); margin: 0 4px; }
  .web-address {
    position: absolute; left: 80px; top: 152px;
    font-family: "Didact Gothic", sans-serif; font-size: 11.5px; color: #fff;
  }

  .info-panel {
    position: absolute; left: 20px; top: 203px; width: 362px; height: 687px;
    background: var(--panel-white); color: var(--ink);
    font-family: "Didact Gothic", sans-serif;
  }
  .product-title {
    position: absolute; left: 26px; top: 22px;
    font-family: "Jost", sans-serif; font-weight: 600; font-size: 16px;
  }
  .uses-list {
    position: absolute; left: 26px; top: 63px; list-style: none;
  }
  .uses-list li {
    font-size: 16px; line-height: 23px; padding-left: 18px; position: relative;
  }
  .uses-list li::before {
    content: ""; position: absolute; left: 1px; top: 10px;
    width: 5px; height: 5px; border-radius: 50%; background: var(--ink);
  }
  .standards-claim {
    position: absolute; left: 22px; top: 372px; width: 320px;
    font-family: "Jost", sans-serif; font-weight: 600; font-size: 20px; line-height: 30px;
  }
  .care-note {
    position: absolute; left: 21px; top: 520px; width: 320px;
    font-size: 10.2px; line-height: 15.3px; text-align: justify;
  }
  .care-note strong { font-family: "Jost", sans-serif; font-weight: 600; }

  .clear-panel {
    position: absolute; left: 0; right: 0; bottom: 0; height: 146px;
    background: linear-gradient(100deg, var(--clear-mid) 0%, var(--clear-light) 30%, #ffffff 55%, var(--clear-light) 80%, var(--clear-mid) 100%);
    border-top: 1px solid var(--clear-edge);
  }
</style>
</head>
<body>
<main class="canvas">
  <section class="polybag">
    <div class="hang-hole"></div>
    <div class="splash-decoration" role="img" aria-label="Blue paint splash decoration"></div>
    <div class="brand-name">karNUsports</div>
    <div class="strapline">PERFORMANCE<span class="divider">|</span>STYLE<span class="divider">|</span>PROTECTION</div>
    <div class="web-address">www.karNUsports.com</div>
    <div class="header-rule"></div>

    <article class="info-panel">
      <h1 class="product-title">STYLISH SPORTS GLASSES</h1>
      <ul class="uses-list">
        <li>Running</li>
        <li>Cycling</li>
        <li>Skiing</li>
        <li>Athletics</li>
        <li>Fishing</li>
        <li>Golf</li>
        <li>Street Sports</li>
        <li>Football</li>
        <li>Cricket</li>
        <li>Hiking</li>
        <li>and Casual Wear</li>
      </ul>
      <h2 class="standards-claim">MEETS OR EXCEEDS ALL CE STANDARDS FOR UV PROTECTION AND FRAME PROTECTION</h2>
      <p class="care-note"><strong>Taking care of your eyewear:</strong> Store at normal room temperature in a box or locker. Transport in the box, bag or case provided and not unprotected with other items. Clean with warm soapy water, rinse then dry with a clean lint free cloth or tissue. Disinfect when required with mild household or medical disinfectant, then rinse off and dry as in previous clause. Check daily; hinge screws, pivots or other moving parts for tightness and security. Broken products, scratched lenses and items obviously at the end of their useful life must be immediately replaced.</p>
    </article>

    <div class="clear-panel"></div>
  </section>
</main>
</body>
</html>
```